Sidewalk Sign For Laundry Service

I'd like to make a sign that offers *free* laundry service for the next customers that bring in their laundry. There needs to be some immediacy in the design. The idea is to put out this sign when we are idle in the laundry and want to use the time to attract new customers. So somehow we need to communicate that the offer is for right now and will likely be gone in an hour or two. Attached are photos of the sign holder in place to give a feel for the location and environment. Obviously I'm looking for a much better design that the one currently in use.

Requirements:
* 23.25" x 35.5" - the full width will be visible but the top and bottom 0.5" will be hidden by the sign holder. It will be printed on coroplast.
* Must include a large arrow to show where the service is offered. We're off the main street so the arrow helps a lot. See the attached pictures of the sign being replaced.
* Needs to be visible to cars as they drive by.
* For the final product I'll need three versions. One with an arrow pointing to the right, one with an arrow pointing to the left, and one to go in the store window with no arrow.

Background on the service: We sort, wash, dry, and fold the laundry for customers and then neatly put it in a nice laundry bag that makes returning very convenient. Their laundry comes out fresh, clean, smelling great, and without the hassle of doing it themselves. We have a great return rate. Most customers that try out the service become long term customers.

Attached are two pictures of the sign holder with our current "Laundry Wash & Fold" sign. Also, our logo which would be nice to include to help with branding.

```html
<!DOCTYPE html>
<html lang="en">
<head>
<meta charset="utf-8">
<title>Free Wash &amp; Fold Service – Sidewalk Sign</title>
<link rel="stylesheet" href="https://fonts.googleapis.com/css2?family=Lobster&family=League+Gothic&family=Yellowtail&display=swap">
<style>
  :root {
    --sign-blue: #1f4ba5;
    --sign-blue-deep: #173d8c;
    --frame-white: #ffffff;
    --sky: #7fd4f6;
    --sky-deep: #4bb8ea;
  }
  html, body {
    margin: 0;
    padding: 0;
    width: 786px;
    height: 1200px;
    overflow: hidden;
    background: var(--sign-blue);
  }
  .sign {
    display: block;
    width: 786px;
    height: 1200px;
  }
  .sign__field { fill: var(--sign-blue); }
  .sign__frame { fill: none; stroke: var(--frame-white); stroke-width: 7; }
  .headline-free {
    font-family: "Lobster", cursive;
    font-size: 230px;
    fill: var(--frame-white);
  }
  .headline-free--shadow { fill: var(--sky-deep); }
  .offer-line {
    font-family: "League Gothic", "Oswald", sans-serif;
    fill: var(--sky);
  }
  .offer-line--shadow { fill: var(--frame-white); }
  .urgency {
    font-family: "Yellowtail", cursive;
    font-size: 190px;
    fill: var(--frame-white);
  }
  .chevron--sky { fill: var(--sky); }
  .chevron--white { fill: var(--frame-white); }
</style>
</head>
<body>
<svg class="sign" viewBox="0 0 786 1200" xmlns="http://www.w3.org/2000/svg" aria-label="Free wash and fold service, now only, with arrow">
  <rect class="sign__field" x="0" y="0" width="786" height="1200"/>
  <rect class="sign__frame" x="28" y="28" width="730" height="1144" rx="4"/>

  <g class="headline">
    <text class="headline-free headline-free--shadow" x="401" y="256" text-anchor="middle" textLength="380" lengthAdjust="spacingAndGlyphs">FREE</text>
    <text class="headline-free" x="393" y="248" text-anchor="middle" textLength="380" lengthAdjust="spacingAndGlyphs">FREE</text>
  </g>

  <g class="offer">
    <text class="offer-line offer-line--shadow" x="399" y="451" font-size="205" text-anchor="middle" textLength="575" lengthAdjust="spacingAndGlyphs">WASH &amp; FOLD</text>
    <text class="offer-line" x="393" y="445" font-size="205" text-anchor="middle" textLength="575" lengthAdjust="spacingAndGlyphs">WASH &amp; FOLD</text>
    <text class="offer-line offer-line--shadow" x="399" y="630" font-size="200" text-anchor="middle" textLength="340" lengthAdjust="spacingAndGlyphs">SERVICE</text>
    <text class="offer-line" x="393" y="624" font-size="200" text-anchor="middle" textLength="340" lengthAdjust="spacingAndGlyphs">SERVICE</text>
  </g>

  <text class="urgency" x="398" y="820" text-anchor="middle" textLength="485" lengthAdjust="spacingAndGlyphs">Now Only!</text>

  <g class="direction-arrow">
    <polygon class="chevron--sky"   points="162,948 232,948 302,1028 232,1108 162,1108 232,1028"/>
    <polygon class="chevron--white" points="232,948 302,948 372,1028 302,1108 232,1108 302,1028"/>
    <polygon class="chevron--sky"   points="302,948 372,948 442,1028 372,1108 302,1108 372,1028"/>
    <polygon class="chevron--white" points="372,948 442,948 512,1028 442,1108 372,1108 442,1028"/>
    <polygon class="chevron--sky"   points="442,948 512,948 582,1028 512,1108 442,1108 512,1028"/>
    <polygon class="chevron--white" points="512,948 580,948 650,1028 580,1108 512,1108 582,1028"/>
  </g>
</svg>
</body>
</html>
```